Postcard Design

Pelumint Frozen Yogurt -- small frozen yogurt/soft serve shop inside Larkwood Plaza. We also have cookies, smoothies and coffee. Frozen Yogurt is self-serve with topping bar and priced by weight. We're locally owned and our cookies and yogurt are all hand made at the store.

We'd like to create a postcard containing 3 or 4 coupons for distribution via direct mail, inclusion in event participant gift bags, etc.

Design-wise, our logo and store feature bright colors (lime green, fuscia, dark purple, orange...) but I'd like to quiet down the overall look of the piece with possibly a brown paper bag and bright accents feel. I'd like the look of the piece to suggest a healthy, quality product.

coupon options: Buy one get one free (equal or lesser value) // save $1 // free waffle cone with froyo purchase // 50% off smoothie

```html
<!DOCTYPE html>
<html lang="en">
<head>
<meta charset="utf-8">
<title>Pelumint Frozen Yogurt Postcard</title>
<link href="https://fonts.googleapis.com/css2?family=Anton&family=Lato:wght@400;700&family=Roboto:wght@400;700&display=swap" rel="stylesheet">
<style>
  :root {
    --purple: #6e2a8c;
    --purple-dark: #5a1f74;
    --yellow-light: #f6e71e;
    --yellow-deep: #f2b71a;
    --green: #5a9a3a;
    --lime: #8cc63f;
    --orange: #f07a21;
    --red-orange: #e0522a;
    --ink: #2b2b2b;
    --white: #ffffff;
    --page: #e4e4e4;
  }
  * { margin: 0; padding: 0; box-sizing: border-box; }
  html, body { width: 806px; height: 1200px; overflow: hidden; }
  body { background: var(--page); position: relative; font-family: 'Lato', sans-serif; }

  .card {
    position: absolute; left: 41px; width: 725px; height: 561px;
    background: var(--white); overflow: hidden;
    box-shadow: 0 2px 6px rgba(0,0,0,0.25);
  }
  .card--front { top: 27px; }
  .card--back { top: 611px; }

  /* Front */
  .brand { position: absolute; left: 29px; top: 58px; display: flex; align-items: center; gap: 14px; }
  .brand__dot { width: 50px; height: 50px; border-radius: 50%; background: var(--orange); flex: none; }
  .brand__name { font-family: 'Lato', sans-serif; font-weight: 700; font-size: 31px; color: var(--purple); white-space: nowrap; }

  .front__stripe { position: absolute; left: 0; top: 182px; width: 330px; height: 11px; background: var(--purple); }
  .front__panel {
    position: absolute; left: 0; top: 193px; width: 725px; height: 311px;
    background: linear-gradient(90deg, var(--yellow-light) 0%, var(--yellow-deep) 70%);
  }
  .front__headline { position: absolute; left: 29px; top: 214px; }
  .headline-strong { font-family: 'Anton', sans-serif; font-size: 27px; color: var(--ink); line-height: 38px; letter-spacing: 0.2px; }
  .headline-light { font-family: 'Roboto', sans-serif; font-size: 27px; color: var(--red-orange); line-height: 36px; }

  .tab {
    position: absolute; left: 0; width: 141px; height: 38px;
    background: linear-gradient(90deg, var(--purple-dark), var(--purple));
    border-radius: 0 19px 19px 0;
    font-family: 'Anton', sans-serif; font-size: 24px; color: var(--white);
    padding-left: 27px; line-height: 38px; letter-spacing: 0.5px;
  }
  .card--front .tab { top: 345px; }
  .card--back .tab { top: 152px; }

  .menu-list { position: absolute; left: 29px; top: 393px; list-style: none; }
  .menu-list li { font-family: 'Lato', sans-serif; font-weight: 700; font-size: 16px; color: var(--ink); line-height: 21px; display: flex; align-items: center; }
  .menu-list li::before { content: ""; width: 6px; height: 6px; border-radius: 50%; background: var(--green); margin-right: 6px; }

  .photo-leaves { position: absolute; left: 0; top: 0; width: 725px; height: 561px; }

  .front__contact {
    position: absolute; left: 0; top: 504px; width: 725px; height: 57px;
    background: var(--green); display: flex; align-items: center; padding-left: 30px; gap: 22px;
  }
  .contact-item { display: flex; align-items: center; gap: 6px; color: var(--white); font-family: 'Lato', sans-serif; font-weight: 700; font-size: 18px; white-space: nowrap; }
  .contact-item svg { flex: none; }

  /* Back */
  .back__panel {
    position: absolute; left: 0; top: 0; width: 351px; height: 482px;
    background: linear-gradient(90deg, var(--yellow-light) 0%, var(--yellow-deep) 100%);
  }
  .back__headline { position: absolute; left: 23px; top: 28px; }
  .back__headline .line-a { font-family: 'Anton', sans-serif; font-size: 21px; color: var(--purple); line-height: 34px; }
  .back__headline .line-b { font-family: 'Roboto', sans-serif; font-size: 28px; color: var(--ink); line-height: 36px; }
  .back__headline .line-c { font-family: 'Roboto', sans-serif; font-size: 23px; color: var(--purple); line-height: 34px; }
  .back__story { position: absolute; left: 23px; top: 208px; width: 232px; font-size: 16px; line-height: 21px; color: var(--ink); text-align: justify; }

  .coupons { position: absolute; left: 30px; top: 329px; display: flex; gap: 12px; }
  .coupon {
    width: 90px; height: 84px; background: var(--purple); border: 2px solid var(--white);
    border-radius: 14px; display: flex; flex-direction: column; align-items: center; justify-content: center;
    text-align: center; font-family: 'Roboto', sans-serif; font-weight: 700; color: var(--white); line-height: 1.15;
  }
  .coupon__big { font-size: 19px; color: var(--yellow-light); }
  .coupon__big--white { color: var(--white); }
  .coupon__small { font-size: 12px; }
  .coupon__accent { color: var(--yellow-light); }
  .coupon__mid { font-size: 16px; color: var(--yellow-light); }

  .back__contact {
    position: absolute; left: 0; top: 482px; width: 374px; height: 79px;
    background: var(--purple); padding: 12px 0 0 23px;
  }
  .back__contact .row { display: flex; gap: 18px; margin-bottom: 8px; }
  .back__contact .contact-item { font-size: 14px; font-weight: 400; }

  .stamp-box { position: absolute; left: 625px; top: 41px; width: 55px; height: 75px; border: 1px solid #555; }
</style>
</head>
<body>

<section class="card card--front">
  <div class="brand">
    <span class="brand__dot"></span>
    <span class="brand__name">Pelumint Frozen Yogurt</span>
  </div>

  <div class="front__stripe"></div>
  <div class="front__panel"></div>

  <div class="front__headline">
    <p class="headline-strong">SMALL FROZEN YOGURT</p>
    <p class="headline-light">SOFT SERVE SHOP</p>
    <p class="headline-strong">INSIDE LARKWOOD PLAZA</p>
  </div>

  <div class="tab">FOODS</div>
  <ul class="menu-list">
    <li>cookies</li>
    <li>smoothies</li>
    <li>coffee</li>
  </ul>

  <svg class="photo-leaves" viewBox="0 0 725 561" xmlns="http://www.w3.org/2000/svg">
    <defs>
      <linearGradient id="coffeeTone" x1="0" y1="0" x2="1" y2="1">
        <stop offset="0" stop-color="#8a6a4e"/><stop offset="1" stop-color="#d9d2c8"/>
      </linearGradient>
      <linearGradient id="smoothieTone" x1="0" y1="0" x2="1" y2="1">
        <stop offset="0" stop-color="#3d4148"/><stop offset="0.6" stop-color="#e9cfa6"/><stop offset="1" stop-color="#2f3338"/>
      </linearGradient>
      <linearGradient id="sundaeTone" x1="0" y1="0" x2="1" y2="1">
        <stop offset="0" stop-color="#f4f1ee"/><stop offset="0.5" stop-color="#d3262e"/><stop offset="1" stop-color="#5a2a1c"/>
      </linearGradient>
    </defs>
    <g role="img" aria-label="Photo of a cup of coffee with coffee beans">
      <path d="M318 218 Q360 150 520 163 Q500 300 425 330 Q340 300 318 218 Z" fill="url(#coffeeTone)" stroke="var(--orange)" stroke-width="7"/>
    </g>
    <g role="img" aria-label="Photo of an orange smoothie in a glass with a straw">
      <path d="M385 472 Q395 290 590 252 Q690 236 740 245 L740 390 Q620 500 385 472 Z" fill="url(#smoothieTone)" stroke="#9b4fb0" stroke-width="7"/>
    </g>
    <g role="img" aria-label="Photo of a frozen yogurt sundae with cherry, chocolate sauce and sprinkles">
      <path d="M493 36 Q700 20 745 320 Q560 310 510 170 Q490 100 493 36 Z" fill="url(#sundaeTone)" stroke="var(--lime)" stroke-width="7"/>
    </g>
  </svg>

  <div class="front__contact">
    <span class="contact-item">
      <svg width="18" height="18" viewBox="0 0 24 24"><path fill="#fff" d="M6.6 10.8a15.1 15.1 0 0 0 6.6 6.6l2.2-2.2c.3-.3.7-.4 1-.2 1.1.4 2.3.6 3.6.6.6 0 1 .4 1 1V20c0 .6-.4 1-1 1A17 17 0 0 1 3 4c0-.6.4-1 1-1h3.5c.6 0 1 .4 1 1 0 1.3.2 2.5.6 3.6.1.3 0 .7-.2 1z"/></svg>
      555-014-2290
    </span>
    <span class="contact-item">
      <svg width="18" height="14" viewBox="0 0 24 18"><rect width="24" height="18" rx="2" fill="#f6e71e"/><path d="M1 2l11 8 11-8" fill="none" stroke="#5a9a3a" stroke-width="2"/></svg>
      hello@pelumintyogurt.com
    </span>
    <span class="contact-item">
      <svg width="16" height="16" viewBox="0 0 24 24"><circle cx="12" cy="12" r="11" fill="#f6e71e"/><path d="M1 12h22M12 1v22M5 5q7 5 14 0M5 19q7-5 14 0" fill="none" stroke="#5a9a3a" stroke-width="1.5"/></svg>
      www.pelumintyogurt.com
    </span>
  </div>
</section>

<section class="card card--back">
  <div class="back__panel"></div>

  <div class="back__headline">
    <p class="line-a">FROZEN YOGURT IS SELF-SERVE</p>
    <p class="line-b">WITH TOPPING BAR</p>
    <p class="line-c">AND PRICED BY WEIGHT</p>
  </div>

  <div class="tab">FOODS</div>
  <p class="back__story">We're locally owned and our cookies and yogurt are all hand made at the store.</p>

  <div class="coupons">
    <div class="coupon">
      <span class="coupon__big">Buy one</span>
      <span class="coupon__small">get one <span class="coupon__accent">free</span></span>
    </div>
    <div class="coupon">
      <span class="coupon__big coupon__big--white">50% off</span>
      <span class="coupon__mid">smoothie</span>
    </div>
    <div class="coupon">
      <span class="coupon__big">save $1</span>
      <span class="coupon__small"><span class="coupon__accent">free</span> waffle</span>
      <span class="coupon__small">cone</span>
    </div>
  </div>

  <div class="back__contact">
    <div class="row">
      <span class="contact-item">
        <svg width="14" height="14" viewBox="0 0 24 24"><path fill="#f6e71e" d="M6.6 10.8a15.1 15.1 0 0 0 6.6 6.6l2.2-2.2c.3-.3.7-.4 1-.2 1.1.4 2.3.6 3.6.6.6 0 1 .4 1 1V20c0 .6-.4 1-1 1A17 17 0 0 1 3 4c0-.6.4-1 1-1h3.5c.6 0 1 .4 1 1 0 1.3.2 2.5.6 3.6.1.3 0 .7-.2 1z"/></svg>
        555-014-2290
      </span>
      <span class="contact-item">
        <svg width="14" height="11" viewBox="0 0 24 18"><rect width="24" height="18" rx="2" fill="#f6e71e"/><path d="M1 2l11 8 11-8" fill="none" stroke="#6e2a8c" stroke-width="2"/></svg>
        hello@pelumintyogurt.com
      </span>
    </div>
    <div class="row">
      <span class="contact-item">
        <svg width="13" height="13" viewBox="0 0 24 24"><circle cx="12" cy="12" r="11" fill="#f6e71e"/><path d="M1 12h22M12 1v22M5 5q7 5 14 0M5 19q7-5 14 0" fill="none" stroke="#6e2a8c" stroke-width="1.5"/></svg>
        www.pelumintyogurt.com
      </span>
    </div>
  </div>

  <div class="stamp-box"></div>
</section>

</body>
</html>
```